Veterinary Hospital Brochure - 2 Drafts - 1 Normal and 1 Fun.

Meadowbrook Pet Hospital needs a brochure to promote our veterinary hospital. These will be delivered to local mailboxes. I would like to see atleast 2 submissions from each designer.
One submission conservative and A4 folded DL and another submission more radical and interesting with innovative folding or crazy concepts. Maybe the brochure could be designed to fold into a dog house ?
I want at least one version to be VERY SIMPLE AND INTIMATE.
Our existing website is here: http://furlane.example/ and our new website will look like this: http://trial4.pagemint.example/#home
Please use colors and images from the new website, and information from the old website. The heading font used in the new site is Qorvatype - Otter Tilt Sketchline
I want the brochure to be simple and engaging on first view, and then provide the opportunity to find more information if desired. The brochure needs to be captivating on the outside so people don't throw it away immediately.

We will soon need letterhead, flags, pens, business cards, signs and vouchers so there is the opportunity for more work for the successful designer.

Target Market(s)

Women 25 to 44

Industry/Entity Type

Veterinary

Contact Information for Business Card

Meadowbrook Pet Hospital
14 Marlow Crescent
Tamsworth Vale
NSW 2417
Phone: 02 61938205
Emergency: 0417360592
Fax: 02 83159462
www.meadowbrookvets.example
contact@meadowbrookvets.example

Font styles to use
Script

Requirements
Must have
• Colors from the new website: http://meadowbrookvets.example/ and new logo.
• Information from the old website: http://furlane.example/
• 2 drafts - A normal A4 folded DL flyer and an interesting crazy design.
Nice to have
• VERY SIMPLE
• Subdued
• Intimate
Should not have
• Intense colours
• Red

```html
<!DOCTYPE html>
<html lang="en">
<head>
<meta charset="utf-8">
<title>Meadowbrook Pet Hospital – DL Brochure</title>
<link href="https://fonts.googleapis.com/css2?family=Dancing+Script:wght@500;600&family=Lato:wght@400;700;900&display=swap" rel="stylesheet">
<style>
  :root{
    --bg:#e6e7ea;
    --paper:#fbf9f6;
    --orange:#ee6a2e;
    --orange-soft:#f39a6c;
    --green:#6c9b3b;
    --green-pale:#dcebd3;
    --brown:#4a3324;
    --text:#6b6560;
    --peach:#f6e3d4;
    --sand:#d9c3a6;
  }
  *{box-sizing:border-box;margin:0;padding:0}
  html,body{width:1200px;height:1158px;overflow:hidden;background:var(--bg)}
  .canvas{position:relative;width:1200px;height:1158px;font-family:"Lato",sans-serif;color:var(--text)}
  .spread{position:absolute;display:flex;box-shadow:0 6px 18px rgba(0,0,0,.14)}
  .spread--inside{left:225px;top:30px}
  .spread--outside{left:350px;top:598px}
  .panel{position:relative;width:250px;height:530px;background:var(--paper);overflow:hidden}
  .panel+.panel{border-left:1px solid rgba(0,0,0,.06)}
  .band{position:absolute;left:0;top:0;width:100%;height:6px;background:var(--orange)}
  .script{font-family:"Dancing Script",cursive;font-weight:500;line-height:1}

  /* services */
  .services{padding:26px 18px 0 16px;background:linear-gradient(180deg,#fdfcfa 0%,#f4efe9 100%)}
  .services h2{color:var(--orange);font-size:42px;margin-bottom:14px}
  .service{display:flex;gap:10px;align-items:flex-start;padding:7px 0 8px;border-bottom:1px solid #e2dcd5}
  .service:last-child{border-bottom:0}
  .service svg{flex:0 0 28px;width:28px;height:28px;margin-top:2px}
  .service h3{font-size:9.5px;font-weight:700;letter-spacing:.2px;text-transform:uppercase;line-height:1.2}
  .service p{font-size:6.8px;line-height:1.35;margin-top:2px}
  .is-green h3,.is-green p{color:var(--green)}
  .is-orange h3,.is-orange p{color:var(--orange)}

  /* middle panel */
  .puppy{background:linear-gradient(180deg,#f7f1ea 0%,#efe6dc 100%)}
  .photo-ring{position:absolute;border-radius:50%;border:5px solid var(--green);box-shadow:0 0 0 3px #fff inset}
  .photo-ring--pup{left:38px;top:42px;width:174px;height:174px;background:radial-gradient(circle at 45% 40%,#e9d6b8 0%,#c8a57a 70%,#b48d63 100%)}
  .puppy h2{position:absolute;left:20px;top:252px;color:var(--orange);font-size:40px}
  .puppy p{position:absolute;left:22px;right:20px;font-size:8.5px;line-height:1.5;color:var(--text)}
  .puppy .p1{top:300px}
  .puppy .p2{top:360px}

  /* pet care */
  .care{padding:40px 20px 0;background:linear-gradient(180deg,#f9f6f1 0%,#f1ebe3 100%)}
  .care h2{color:var(--green);font-size:38px;text-align:center;margin-bottom:14px}
  .care .lead{font-size:8.2px;line-height:1.5;text-align:center;margin-bottom:12px}
  .care ul{list-style:none;padding-left:18px}
  .care li{color:var(--green);font-size:9.5px;line-height:1.55;display:flex;align-items:center;gap:6px}
  .care li::before{content:"";width:6px;height:6px;border-radius:50%;background:var(--green);flex:0 0 6px}
  .photo-ring--cat{left:62px;top:372px;width:150px;height:150px;border-color:var(--orange);background:radial-gradient(circle at 55% 45%,#d8a574 0%,#b87c4a 65%,#8c5a34 100%)}

  /* back panel */
  .back{background:linear-gradient(180deg,#fdf6ef 0%,var(--peach) 70%,#efdcc9 100%);text-align:center}
  .wordmark{display:flex;align-items:center;justify-content:center;gap:7px;color:var(--brown);font-family:"Lato",sans-serif;font-weight:900;text-transform:uppercase;letter-spacing:.5px}
  .wordmark .dot{width:10px;height:10px;border-radius:50%;background:var(--green)}
  .back .wordmark{margin-top:40px;font-size:14px;line-height:1.15;text-align:left}
  .contact{margin-top:26px;color:var(--brown);font-size:10px;line-height:1.55;font-weight:700}
  .contact .gap{height:12px}
  .social{display:inline-flex;align-items:center;gap:5px}
  .social i{width:8px;height:8px;background:var(--orange);display:inline-block}
  .map{position:absolute;left:50px;top:338px;width:150px;height:150px;border-radius:50%;border:5px solid var(--green);background:linear-gradient(135deg,#f1f1ef,#dfe0dc)}

  /* cover */
  .cover{background:linear-gradient(180deg,#cfe3c4 0%,#dcebd1 40%,#eef1dc 60%,#f4ecd9 100%)}
  .cover .band{background:var(--orange)}
  .cover-head{position:absolute;left:0;top:6px;width:100%;height:112px;background:rgba(200,224,188,.7);display:flex;align-items:center;justify-content:center}
  .cover .wordmark{font-size:17px;line-height:1.1;text-align:left}
  .tagline{position:absolute;left:0;top:140px;width:100%;text-align:center}
  .tagline .big{display:block;color:var(--orange);font-size:52px}
  .tagline .small{display:block;color:var(--brown);font-size:28px;line-height:1.15;margin-top:4px}
  .cover-photo{position:absolute;left:0;bottom:0;width:100%;height:268px;background:linear-gradient(180deg,rgba(235,228,205,0) 0%,#c9a988 30%,#8f6a4c 70%,#5a4333 100%)}
</style>
</head>
<body>
<div class="canvas">

  <section class="spread spread--inside" aria-label="Brochure inside">
    <article class="panel services">
      <div class="band"></div>
      <h2 class="script">Services</h2>

      <div class="service is-green">
        <svg viewBox="0 0 28 28"><circle cx="14" cy="9" r="5" fill="#6c9b3b"/><path d="M5 26c0-6 4-10 9-10s9 4 9 10z" fill="#6c9b3b"/></svg>
        <div><h3>Companion Animal Surgery</h3><p>Meadowbrook Pet Hospital has the latest surgical instrumentation and anaesthetic monitoring to ensure the success of surgery and outcomes for your pets.</p></div>
      </div>
      <div class="service is-orange">
        <svg viewBox="0 0 28 28"><g transform="rotate(-35 14 14)"><rect x="4" y="9" width="20" height="10" rx="5" fill="#ee6a2e"/><rect x="14" y="9" width="10" height="10" rx="5" fill="#f39a6c"/></g></svg>
        <div><h3>Companion Animal Medecine</h3><p>Our diagnostic facilities enable us to identify disease rapidly and treat promptly with the correct therapies.</p></div>
      </div>
      <div class="service is-green">
        <svg viewBox="0 0 28 28"><circle cx="14" cy="15" r="9" fill="#6c9b3b"/><path d="M6 7l8-4 8 4-8 4z" fill="#4a3324"/></svg>
        <div><h3>Puppy School</h3><p>Puppy Pre-School is an essential first step for all puppies regardless of breed or owner education.</p></div>
      </div>
      <div class="service is-orange">
        <svg viewBox="0 0 28 28"><path d="M14 4c6.6 0 12 4.2 12 9.5S20.6 23 14 23c-1.4 0-2.7-.2-3.9-.5L4 25l2-5C3.5 18.3 2 16 2 13.5 2 8.2 7.4 4 14 4z" fill="#ee6a2e"/><circle cx="9" cy="13.5" r="1.6" fill="#fff"/><circle cx="14" cy="13.5" r="1.6" fill="#fff"/><circle cx="19" cy="13.5" r="1.6" fill="#fff"/></svg>
        <div><h3>Follow Ups and Reminders</h3><p>Meadowbrook Pet Hospital has the latest surgical instrumentation and anaesthetic monitoring to ensure care.</p></div>
      </div>
      <div class="service is-green">
        <svg viewBox="0 0 28 28"><rect x="12" y="3" width="5" height="14" rx="1" fill="#6c9b3b" transform="rotate(-20 14 10)"/><path d="M6 25h16M9 21h8" stroke="#6c9b3b" stroke-width="3" stroke-linecap="round"/></svg>
        <div><h3>Laboratory</h3><p>Our in-house laboratory gives fast, accurate test results so treatment can begin the same day.</p></div>
      </div>
      <div class="service is-orange">
        <svg viewBox="0 0 28 28"><rect x="5" y="4" width="18" height="20" rx="4" fill="#ee6a2e"/><path d="M9 9h10M9 13h10M9 17h10" stroke="#fff" stroke-width="1.6"/></svg>
        <div><h3>Radiology</h3><p>Digital x-ray and ultrasound let us look closely inside and diagnose with confidence.</p></div>
      </div>
      <div class="service is-green">
        <svg viewBox="0 0 28 28"><path d="M5 6l5 5h8l5-5v13a9 7 0 0 1-18 0z" fill="#6c9b3b"/></svg>
        <div><h3>Feline Friendly</h3><p>Meadowbrook Pet Hospital has the latest instrumentation and a quiet cat-only area to ensure the success of surgery and outcomes.</p></div>
      </div>
    </article>

    <article class="panel puppy">
      <div class="band"></div>
      <div class="photo-ring photo-ring--pup" role="img" aria-label="Photo of a puppy giving a high five to a hand"></div>
      <h2 class="script">Puppy School</h2>
      <p class="p1">Puppy School is so much fun, your puppy will have a ball while learning and socialising with other pups in a safe, friendly setting.</p>
      <p class="p2">Topics include toilet training, chewing, play biting, basic commands, grooming and good healthy habits for life.</p>
    </article>

    <article class="panel care">
      <div class="band"></div>
      <h2 class="script">Pet Care Basics</h2>
      <p class="lead">Meadowbrook Pet Hospital provides gold standard pet health care. This means we offer you the best possible care and remind you when it is due. This includes:</p>
      <ul>
        <li>Yearly Vaccination and Checkup</li>
        <li>Microchipping</li>
        <li>Premium Food</li>
        <li>Heartworming</li>
        <li>Socialisation</li>
        <li>Intestinal Worming</li>
        <li>Sterilisation</li>
        <li>Flea Treatment</li>
        <li>Dental Care</li>
        <li>Weight Management</li>
      </ul>
      <div class="photo-ring photo-ring--cat" role="img" aria-label="Photo of a ginger cat lying down"></div>
    </article>
  </section>

  <section class="spread spread--outside" aria-label="Brochure outside">
    <article class="panel back">
      <div class="band"></div>
      <div class="wordmark"><span class="dot"></span><span>Meadowbrook Pet<br>Hospital</span></div>
      <div class="contact">
        <div>14 Marlow Cres, Tamsworth Vale</div>
        <div>NSW 2417.</div>
        <div class="gap"></div>
        <div>Phone: 6193 8205</div>
        <div>Fax: 83159462</div>
        <div>email: contact@furlane.example</div>
        <div>www.furlane.example</div>
        <div class="social"><i></i>Meadowbrook PetHospital</div>
        <div class="gap"></div>
        <div>Monday to Friday - 8:30am to 6:00pm</div>
        <div>Saturday - 9:00am to 12:00pm</div>
      </div>
      <div class="map" role="img" aria-label="Street map showing the hospital location"></div>
    </article>

    <article class="panel cover">
      <div class="band"></div>
      <div class="cover-head"><div class="wordmark"><span class="dot"></span><span>Meadowbrook Pet<br>Hospital</span></div></div>
      <div class="tagline">
        <span class="script big">Kindness,</span>
        <span class="script small">when you need<br>it most</span>
      </div>
      <div class="cover-photo" role="img" aria-label="Photo of a woman hugging her dog"></div>
    </article>
  </section>

</div>
</body>
</html>
```